Wordpress Design for Interactive Marketing Agency

We are looking to have a WP theme designed for our company, Bright Lantern Media. We are an online marketing firm specializing in SEO, Paid Search/PPC, Analytics and a number of other marketing channels.
We have a logo and tag line. We also have a rough and unloved design to work from as a way to illustrate the content needs of the homepage. We would like an interactive slider on the homepage which displays text and image content describing our services and our value props/solution positioning. Layering content is also something we'd like to incorporate in a block or two on the page, whether it be tabs, window shades, rotating or mouse-over type div swapping, scrolling news box, etc.
The design also needs to be able to transition to a less portal-like feel (re: the homepage) to a page design that houses a description for each of our services, an about page, privacy page, etc.
So, in the spirit of the typical WP construct, there would be a consistent header and footer, with a main content div that is flexible and eye-catching.
Three column design for the homepage feels right, but that's not a requirement. For the rest of the pages one or two columns seems like the right layout. Again, is this open to design.
To see what we've put together as a concept visit this page:
www.brightlanternmedia.example/design/
Notes: most folks didn't care for the opaque gun in the background. Though, a subtle, muted background image would be a welcome design element. Keep in mind that these images are only for illustrating the content needs. We are not expecting anything that looks like these concepts. In fact, they didn't appeal to most of us.
Also included is a third design that we kind of liked (probably could live without the page curls, though). Modern sophistication that isn't stuffy but doesn't get too juvenile is what we're wanting. If there's a way to complement the power colors of our logo and attain a style that's lively, digerati in spirit and alluring, then that's what we would like to arrive at.
To get the latest logo:
http://brightlanternmedia.example/design/Logo-Rework.png
The logo can be rearranged as needed.
I have also attached the rough designs we put together and the logo.
We really don't have any strong restrictions or absolutes as far as how the design turns out. We just want something that looks great and captures the spirit of the business/brand. The visuals could definitely benefit from a human element, or a splashy graphic or something festive, technically inclined and/or inclusive.
Updates
Project Deadline Extended
Reason: I am trying to make the project a little more accessible for designers by extending it a bit. I realize that the process can sometimes take several days, and if this allows for more submissions, there are no complaints here.
Hi Designers,
Target Market(s)
Medium-sized, regional businesses
Industry/Entity Type
Marketing
Requirements
Must have
- Theme must accomodate widgets, permalinks and all of the common WP page enhancements and taxonomy options.
Nice to have
- Most of the text on the page should be true text if possible (for SEO purposes, etc.). The ability to layer text content is also desirable, so having content blocks that use z-indexed divs would be ideal. Theme should accommodate widgets, permalinks and all of the common WP page enhancements and taxonomy options.

```html
<!DOCTYPE html>
<html lang="en">
<head>
<meta charset="utf-8">
<title>Bright Lantern Media — Online Marketing</title>
<link rel="stylesheet" href="https://fonts.googleapis.com/css2?family=Ubuntu:wght@300;400;500;700&family=Questrial&family=Arimo:ital,wght@0,400;0,700;1,700&display=swap">
<style>
:root{
  --red:#e23b24;
  --dark:#2b2b2b;
  --text:#222;
  --muted:#777;
  --band:#e6e6e6;
  --page:#efefef;
  --panel:#ffffff;
  --field:#4d4d4d;
  --line:#d6d6d6;
  --badge:#f6f6f6;
}
*{box-sizing:border-box;margin:0;padding:0}
html,body{width:1121px;height:1200px;overflow:hidden}
body{position:relative;background:var(--page);font-family:"Ubuntu",sans-serif;color:var(--text)}
.abs{position:absolute}
a{color:inherit;text-decoration:none}

/* top bar */
.topbar{left:0;top:0;width:1121px;height:41px;background:var(--dark);color:#fff}
.topnav{left:103px;top:0;height:41px;display:flex;align-items:center;gap:17px;font-size:12px}
.topcall{left:520px;top:0;height:41px;display:flex;align-items:center;gap:20px;font-size:17px;font-weight:400;letter-spacing:.2px}
.search{left:842px;top:3px;width:176px;height:35px;background:#fff;border:1px solid #999;font-size:11px;font-style:italic;color:#666;padding:0 10px;display:flex;align-items:center;justify-content:space-between}

/* header */
.header{left:0;top:41px;width:1121px;height:131px;background:var(--band)}
.brand{left:103px;top:74px}
.brand-name{display:flex;align-items:center;gap:10px;font-family:"Ubuntu",sans-serif;font-weight:700;font-size:24px;color:var(--red);letter-spacing:1px;text-transform:uppercase}
.brand-dot{width:30px;height:30px;border-radius:50%;background:var(--red)}
.brand-tag{margin-left:40px;margin-top:4px;font-size:13px;font-weight:500;color:#666;letter-spacing:.4px}
.headline{left:467px;top:92px;font-family:"Arimo",sans-serif;font-weight:700;font-size:19px;color:#111}
.badge{top:68px;width:62px;height:76px;background:var(--badge);border:1px solid #cfcfcf;border-radius:2px}

/* main panel */
.panel{left:103px;top:202px;width:915px;height:394px;background:var(--panel);border:1px solid #dcdcdc}
.panel-shadow{left:150px;top:590px;width:820px;height:30px;border-radius:50%;background:radial-gradient(ellipse at center,rgba(0,0,0,.16),rgba(0,0,0,0) 70%)}
.tabs{left:121px;top:186px;height:71px;display:flex;font-size:11.5px;font-weight:500}
.tab{height:71px;display:flex;align-items:flex-end;padding-bottom:21px}
.tab.active{width:78px;background:var(--red);color:#fff;justify-content:center;position:relative}
.tab.active::after{content:"";position:absolute;right:-9px;top:0;border-left:9px solid #a82816;border-top:14px solid transparent}

.slider{left:121px;top:262px;width:603px;height:315px;border:2px solid #dedede;background:#fff}
.slide-title{left:10px;top:58px;font-family:"Arimo",sans-serif;font-weight:700;font-size:19px;color:var(--red)}
.slide-copy{left:9px;top:110px;width:292px;font-family:"Questrial",sans-serif;font-size:17px;line-height:30.5px;color:#7a7a7a;text-align:justify}
.slide-art{left:309px;top:8px;width:292px;height:238px;background:linear-gradient(150deg,#dfeaf5 0%,#c7dcef 55%,#e8eef4 100%)}
.slide-nav{top:278px;width:34px;height:34px;border-radius:50%;background:#222}

.contact-title{left:749px;top:254px;font-family:"Ubuntu",sans-serif;font-weight:300;font-size:44px;color:var(--red);line-height:1}
.contact-title b{font-weight:300;font-size:74px;vertical-align:-6px}
.field{left:749px;width:245px;background:linear-gradient(#6a6a6a,#3e3e3e);color:#fff;font-family:"Arimo",sans-serif;font-size:10.5px;font-style:italic;padding:6px 9px;border-bottom:2px solid #ccc}
.send{left:925px;top:553px;width:69px;height:25px;background:var(--red);color:#fff;font-family:"Arimo",sans-serif;font-weight:700;font-size:13px;display:flex;align-items:center;justify-content:center}

/* services band */
.services{left:103px;top:661px;width:915px;height:170px;background:#e8e8e8;border:1px solid #dedede}
.svc-list{list-style:none;font-size:13.5px;line-height:22px;color:#111}
.svc-list li{position:relative;padding-left:15px}
.svc-list li::before{content:"";position:absolute;left:0;top:8px;width:6px;height:6px;border-radius:50%;background:var(--red)}
.svc-shot{width:126px;height:118px;background:#fff;border:1px solid #ccc;box-shadow:3px 3px 4px rgba(0,0,0,.18);padding:8px}
.svc-shot span{display:block;width:100%;height:100%}

/* content */
.content{left:0;top:880px;width:1121px;height:265px;background:#fff}
.section-title{font-family:"Ubuntu",sans-serif;font-weight:500;font-size:20px;color:var(--red)}
.rule{height:1px;background:var(--line)}
.welcome-body{left:104px;top:959px;width:595px;font-family:"Arimo",sans-serif;font-size:10.5px;line-height:14px;color:#111}
.welcome-body p{margin-bottom:13px}
.welcome-body .lead{font-weight:700;font-style:italic;text-align:justify;letter-spacing:.2px}
.projects{left:743px;top:951px;width:275px;height:146px}
.thumb{width:61px;height:61px}
.vsep{width:1px;background:var(--line)}

/* footer */
.footer{left:0;top:1145px;width:1121px;height:55px;background:var(--page);border-top:1px solid #ddd}
.footnav{left:104px;top:1161px;display:flex;gap:15px;font-size:10px;color:#222}
.copy{left:104px;top:1175px;font-size:10px;color:#222}
.social{top:1160px;width:26px;height:26px;border-radius:4px}
.accredit{left:926px;top:1156px;width:92px;height:34px;background:#d9d9d9;border:1px solid #c4c4c4;border-radius:3px}
</style>
</head>
<body>

<header>
  <div class="abs topbar"></div>
  <nav class="abs topnav" style="color:#fff">
    <a href="#">Privacy Policy</a><a href="#">Terms of Service</a><a href="#">About Us</a><a href="#">Contact Us</a><a href="#">Our Blog</a>
  </nav>
  <div class="abs topcall" style="color:#fff"><span>1800 555 0199</span><span>GET A FREE AUDIT</span></div>
  <div class="abs search"><span>Search...</span>
    <svg width="16" height="16" viewBox="0 0 16 16"><circle cx="6.5" cy="6.5" r="4.6" fill="none" stroke="#222" stroke-width="2"/><line x1="10" y1="10" x2="14.5" y2="14.5" stroke="#222" stroke-width="2.6" stroke-linecap="round"/></svg>
  </div>

  <div class="abs header"></div>
  <div class="abs brand">
    <div class="brand-name"><span class="brand-dot"></span>Bright Lantern Media</div>
    <div class="brand-tag">Online Marketing. Brightly Done.</div>
  </div>
  <h1 class="abs headline">Online Marketing Dallas Austin Houston</h1>
  <div class="abs badge" style="left:876px" role="img" aria-label="Certified partner badge"></div>
  <div class="abs badge" style="left:946px" role="img" aria-label="Certified partner badge"></div>
</header>

<main>
  <div class="abs panel-shadow"></div>
  <section class="abs panel"></section>
  <nav class="abs tabs">
    <span class="tab active">Paid Search</span>
    <span class="tab" style="margin-left:45px">SEO</span>
    <span class="tab" style="margin-left:63px">Dispay Ads</span>
    <span class="tab" style="margin-left:45px">Analytics</span>
    <span class="tab" style="margin-left:37px">Performance</span>
  </nav>

  <div class="abs slider">
    <h2 class="abs slide-title">Are you on the map?</h2>
    <p class="abs slide-copy">We can get you there with our Local SEO service. Local SEO is essential to your online marketing. We help you expand your local presence in SEO and beyond.</p>
    <div class="abs slide-art" role="img" aria-label="Illustration of a folded city map with a red location pin"></div>
    <svg class="abs slide-nav" style="left:535px" viewBox="0 0 34 34"><circle cx="17" cy="17" r="17" fill="#222"/><path d="M21 10 L11 17 L21 24 Z" fill="#fff"/></svg>
    <svg class="abs slide-nav" style="left:572px" viewBox="0 0 34 34"><circle cx="17" cy="17" r="17" fill="#222"/><path d="M13 10 L23 17 L13 24 Z" fill="#fff"/></svg>
  </div>

  <h2 class="abs contact-title"><b>C</b>ontact Us</h2>
  <div class="abs field" style="top:328px;height:23px">Name</div>
  <div class="abs field" style="top:370px;height:23px">Email</div>
  <div class="abs field" style="top:409px;height:133px">How can we help you?</div>
  <a class="abs send" href="#">Send</a>

  <section class="abs services"></section>
  <ul class="abs svc-list" style="left:121px;top:679px">
    <li>Local Seo</li><li>Link Building</li><li>Content</li><li>Design</li><li>Development</li><li>Mobile</li>
  </ul>
  <div class="abs svc-shot" style="left:266px;top:685px"><span role="img" aria-label="Two smartphones showing search results and a map" style="background:linear-gradient(90deg,#3a3a3a,#9aa3ad 50%,#3a3a3a)"></span></div>
  <ul class="abs svc-list" style="left:408px;top:679px">
    <li>Attribution Tracking</li><li>Call Tracking</li><li>Pay for Performance</li><li>Affiliate Marketing</li><li>Retargeting</li><li>Landing Page Testing</li>
  </ul>
  <div class="abs svc-shot" style="left:572px;top:685px"><span role="img" aria-label="Diagram of marketing channel paths" style="background:linear-gradient(#f6f2f2,#eef3f7)"></span></div>
  <ul class="abs svc-list" style="left:716px;top:679px">
    <li>Social Media</li><li>Video Commerce</li><li>Custom Analytics</li><li>Custom Reporting</li><li>Retargeting</li>
  </ul>
  <div class="abs svc-shot" style="left:872px;top:685px"><span role="img" aria-label="Analytics dashboard report page" style="background:linear-gradient(#f1f1f1,#dfe6ee)"></span></div>

  <section class="abs content"></section>
  <h2 class="abs section-title" style="left:104px;top:906px">Welcome to Bright Lantern Media</h2>
  <div class="abs rule" style="left:104px;top:943px;width:595px"></div>
  <div class="abs welcome-body">
    <p class="lead">Bright lantern media is a full-service Internet markting agency providing Paid Search (PPC), Search Engine Optimization (SEO), Display Advertising,Analytics Consulting, Creative Direction, and ...</p>
    <p>Lorem Ipsum is simply dummy text of the printing and typesetting industry. Lorem Ipsum has been the industry's standard dummy text ever since the 1500s.</p>
    <p>&nbsp;when an unknown printer took a galley of type and scrambled it to make a type specimen book. It has survived not only five centuries, but also the leap into electronic typesetting, remaining essentially unchanged.</p>
    <p>It was popularised in the 1960s with the release of Lettrix sheets containing Lorem Ipsum passages, and more recently with desktop publishing software like Pagewright including versions of Lorem Ipsum.</p>
  </div>

  <h2 class="abs section-title" style="left:743px;top:906px;font-size:17px">Latest Projects</h2>
  <div class="abs rule" style="left:743px;top:943px;width:275px"></div>
  <div class="abs projects">
    <div class="abs thumb" style="left:0;top:0;background:linear-gradient(#eef6fb,#3aa7d8)" role="img" aria-label="Project screenshot"></div>
    <div class="abs thumb" style="left:107px;top:0;background:linear-gradient(#f3f3f3,#d9d9d9)" role="img" aria-label="Project screenshot"></div>
    <div class="abs thumb" style="left:214px;top:0;background:linear-gradient(#3e4a3a,#5c8f2e)" role="img" aria-label="Project screenshot"></div>
    <div class="abs thumb" style="left:0;top:86px;background:linear-gradient(#2e2e2e,#d9842a)" role="img" aria-label="Project screenshot"></div>
    <div class="abs thumb" style="left:107px;top:86px;background:linear-gradient(#f4f7f9,#4ab3d8)" role="img" aria-label="Project screenshot"></div>
    <div class="abs thumb" style="left:214px;top:86px;background:linear-gradient(#1f2a1c,#6aa236)" role="img" aria-label="Project screenshot"></div>
    <div class="abs vsep" style="left:84px;top:0;height:146px"></div>
    <div class="abs vsep" style="left:191px;top:0;height:146px"></div>
    <div class="abs rule" style="left:0;top:73px;width:275px"></div>
  </div>
</main>

<footer>
  <div class="abs footer"></div>
  <nav class="abs footnav"><a href="#">Privacy Policy</a><a href="#">Terms of Service</a><a href="#">About Us</a><a href="#">Contact Us</a><a href="#">Our Blog</a></nav>
  <div class="abs copy">© Copyrights 2012 All rights Reserved</div>
  <div class="abs social" style="left:806px;background:#3b5e9a" role="img" aria-label="Social profile link"></div>
  <div class="abs social" style="left:843px;background:#4db4e6" role="img" aria-label="Social profile link"></div>
  <div class="abs social" style="left:880px;background:#1d4f86" role="img" aria-label="Business listing link"></div>
  <div class="abs accredit" role="img" aria-label="Accreditation badge"></div>
</footer>

</body>
</html>
```